Commercial Bakery needs packing design for a Bread Bag.

Brenton's Bakery needs a design for a bread bag to be distributed to grocery stores. We make all kinds of breads and want this packaging to represent our company. We would like the packaging to be black and white with a fun/bubbly modern design. I have attached a few ideas of what I am looking for.
There are 5 different products. Packaging must be the same for each product except for corresponding product name, bar code and nutrional facts.
Product names:
Coconut Cream Bread
Cream Bread
Potato Rolls
Roll ups
Coconut & Raisin Bread

Our products are packaged in a 11” x 8” poly bag.
I will open 5 contracts with whoever’s design I select. I will then provide nutritional facts, barcodes for items once a contract is selected. Thank you!!

Target Market(s)

Grocery stores

Industry/Entity Type

Bakery

Requirements
Must have
• Black and White (off whites are ok)
Should not have
• Color

```html
<!DOCTYPE html>
<html lang="en">
<head>
<meta charset="UTF-8">
<title>Brenton's Bakery – Coconut Cream Bread Bag</title>
<link href="https://fonts.googleapis.com/css2?family=Montserrat:wght@500;600;800&family=Libre+Baskerville:wght@700&display=swap" rel="stylesheet">
<style>
  :root {
    --stage: #b9b9b9;
    --bag-white: #ececed;
    --bag-white-top: #f7f7f8;
    --ink: #1b1b1b;
    --paper: #ffffff;
    --crumb-light: #e2a04a;
    --crumb-mid: #c97b2c;
    --crumb-dark: #8f4a18;
    --ornament-tone: #cfcfd1;
  }
  * { margin: 0; padding: 0; box-sizing: border-box; }
  html, body {
    width: 1100px;
    height: 1200px;
    overflow: hidden;
    background: var(--stage);
  }
  .bag-front {
    position: absolute;
    left: 170px;
    top: 70px;
    width: 760px;
    height: 1060px;
    background: linear-gradient(180deg, var(--bag-white-top) 0%, var(--bag-white) 100%);
    border-radius: 40px 40px 0 0;
    overflow: hidden;
  }
  .bread-window {
    position: absolute;
    left: 0;
    top: 410px;
    width: 100%;
    height: 270px;
    background:
      radial-gradient(ellipse at 50% 45%, var(--crumb-light) 0%, var(--crumb-mid) 55%, var(--crumb-dark) 100%);
  }
  .grain-tab {
    position: absolute;
    left: 120px;
    top: 90px;
    width: 80px;
    height: 460px;
    background: var(--ink);
    border-radius: 0 0 10px 10px;
    display: flex;
    align-items: center;
    justify-content: center;
  }
  .grain-tab__label {
    transform: rotate(-90deg);
    white-space: nowrap;
    font-family: "Montserrat", sans-serif;
    font-weight: 600;
    font-size: 36px;
    letter-spacing: 1px;
    color: var(--paper);
  }
  .brand-mark {
    position: absolute;
    left: 430px;
    top: 290px;
    display: flex;
    align-items: center;
    gap: 14px;
  }
  .brand-mark__dot {
    width: 22px;
    height: 22px;
    border-radius: 50%;
    background: var(--ink);
    flex: none;
  }
  .brand-mark__name {
    font-family: "Montserrat", sans-serif;
    font-weight: 800;
    font-size: 38px;
    line-height: 1.05;
    color: var(--ink);
    text-transform: uppercase;
  }
  .product-title {
    position: absolute;
    left: 0;
    width: 100%;
    top: 720px;
    text-align: center;
  }
  .product-title__rule {
    display: block;
    margin: 0 auto;
    height: 2px;
    background: var(--ink);
  }
  .product-title__rule--wide { width: 360px; }
  .product-title__rule--narrow { width: 230px; margin-top: 10px; }
  .product-title__rule--narrow-bottom { width: 230px; margin-bottom: 10px; }
  .product-title__name {
    font-family: "Libre Baskerville", serif;
    font-weight: 700;
    font-size: 46px;
    line-height: 1.15;
    color: var(--ink);
    margin: 34px 0 40px;
  }
  .flourish {
    position: absolute;
    top: 770px;
    width: 40px;
    height: 110px;
    border-radius: 20px;
    background: var(--ornament-tone);
  }
  .flourish--left { left: 60px; }
  .flourish--right { right: 60px; }
  .net-weight-band {
    position: absolute;
    left: 0;
    bottom: 0;
    width: 100%;
    height: 70px;
    background: var(--ink);
    display: flex;
    align-items: center;
    justify-content: center;
    font-family: "Montserrat", sans-serif;
    font-weight: 500;
    font-size: 17px;
    letter-spacing: 1px;
    color: var(--paper);
  }
</style>
</head>
<body>
  <main class="bag-front">
    <div class="bread-window" role="img" aria-label="Close-up photograph of golden toasted bread crumb"></div>

    <div class="grain-tab"><span class="grain-tab__label">HEALTHY GRAIN</span></div>

    <div class="brand-mark">
      <span class="brand-mark__dot"></span>
      <span class="brand-mark__name">Brenton's<br>Bakery</span>
    </div>

    <div class="flourish flourish--left" role="img" aria-label="Decorative scroll ornament"></div>
    <div class="flourish flourish--right" role="img" aria-label="Decorative scroll ornament"></div>

    <section class="product-title">
      <span class="product-title__rule product-title__rule--narrow-bottom"></span>
      <span class="product-title__rule product-title__rule--wide"></span>
      <h1 class="product-title__name">COCONUT<br>CREAM BREAD</h1>
      <span class="product-title__rule product-title__rule--wide"></span>
      <span class="product-title__rule product-title__rule--narrow"></span>
    </section>

    <footer class="net-weight-band">NET WT 15OZ (425g)</footer>
  </main>
</body>
</html>
```